3 out of 100 people will get deadly skin cancer - we need a great illustration that shows this!

We put together a prototype image that communicates lifetime skin cancer risk. (see attached). We are looking for illustrators who can take make a new/better/cooler graphic that communicates this idea. It could be as simple as a superior illustration of the graphic we have or illustrators can propose a completely different idea.What should the illustration communicate?U.S. adults have a lifetime risk of developing skin cancer of 1 in 5. But we don't want to show 1 in 5; we want to show that number in a larger group. For example, in the attached illustration we show 20 in 100 people get skin cancer (i.e., 100 beach towels/umbrellas and 20 of them are red). Research has shown that people are more likely to accurately understand numbers like this when you convey them for larger groups (i.e., 20 out of 100 rather than 1 out of 5). U.S. adults also have a lifetime risk of 2.3% of developing the deadliest form of skin cancer (melanoma). In other words, approximately 3 in 100 people will develop melanoma in their lifetime. Ideally, a single image will convey both lifetime skin cancer risk (20 in 100) and melanoma risk (3 in 100). We will award a top three as follows: 1st place = $300, 2nd place = $250, third place = $200. We will also buy any design beyond 3rd place that we like for $100. For example, we purchased 24 designs in our last contest on Artmarketly.This research is supported by funding from the Corvane Institute of Science.

Target Market(s)

The U.S. public; individuals at high risk of developing skin cancer

Industry/Entity Type

Medicine

Colors

Designer to choose colors to be used in the design.

Requirements
Must have
• an original illustration that conveys both lifetime risk of developing skin cancer (20 in 100) and melanoma (3 in 100).
Nice to have
• It can be beach towels and umbrellas, just like our prototype, or the designers can pitch an original idea. Imagery can be realistic or cartoonish (or something in between). It should be illustrations, though. Not edited photos. The image should be in color (no black and white illustrations).
Should not have
• Photos. Clip art. Free vector images.
• We are looking for original illustrations created by the designer.

```html
<!DOCTYPE html>
<html lang="en">
<head>
<meta charset="utf-8">
<title>How likely are you to get skin cancer?</title>
<link href="https://fonts.googleapis.com/css2?family=Anton&family=Questrial&display=swap" rel="stylesheet">
<style>
  :root {
    --ink: #4a4e70;
    --sand-top: #f6a44a;
    --sand-mid: #f9b86c;
    --sand-bottom: #fccf98;
    --sun: #f08a2a;
    --sun-dark: #e06a1c;
    --towel-clear: #bfdcef;
    --towel-skin: #dcc38f;
    --towel-melanoma: #d8774f;
    --sea-light: #62d8ec;
    --sea-deep: #35c2ee;
    --foam: #ffffff;
  }
  * { margin: 0; padding: 0; box-sizing: border-box; }
  html, body { width: 1200px; height: 3628px; overflow: hidden; }
  body {
    position: relative;
    background: linear-gradient(180deg, var(--sand-top) 0%, var(--sand-mid) 45%, var(--sand-bottom) 86%);
    color: var(--ink);
    font-family: "Questrial", "Helvetica Neue", Arial, sans-serif;
  }
  .headline {
    position: absolute; left: 56px; top: 58px;
    font-family: "Anton", "Impact", sans-serif;
    font-weight: 400; font-size: 72px; line-height: 1;
    letter-spacing: -0.5px; white-space: nowrap;
  }
  .intro {
    position: absolute; left: 57px; top: 162px;
    font-size: 38px; line-height: 59px; letter-spacing: 0.3px;
  }
  .sun-art {
    position: absolute; left: 80px; top: 396px; width: 370px; height: 460px;
    border-radius: 50% 50% 40% 40%;
    background: radial-gradient(circle at 50% 38%, var(--sun) 0 34%, var(--sun-dark) 35% 50%, rgba(240,138,42,0) 51%);
  }
  .legend { position: absolute; left: 563px; top: 443px; }
  .legend-row { display: flex; align-items: center; height: 127px; margin-bottom: 14px; }
  .legend-tiles { display: flex; gap: 18px; margin-right: 28px; }
  .legend-tiles .towel { width: 62px; height: 127px; }
  .legend-label { font-size: 51px; letter-spacing: 0.5px; }
  .beach-grid {
    position: absolute; left: 73px; top: 1040px;
    display: grid; grid-template-columns: repeat(10, 82px);
    column-gap: 23px; row-gap: 24px;
  }
  .beach-grid .towel { width: 82px; height: 169px; }
  .towel { background: var(--towel-clear); }
  .towel.skin { background: var(--towel-skin); }
  .towel.melanoma { background: var(--towel-melanoma); }
  .shore { position: absolute; left: 0; top: 3120px; width: 1200px; height: 508px; }
</style>
</head>
<body>
  <h1 class="headline">How likely are you to get skin cancer?</h1>
  <p class="intro">Let's say 100 people go to the beach<br>How many will develop skin cancer in their lifetime?<br>How many melanoma,the deadliest form of skin cancer?</p>

  <div class="sun-art" role="img" aria-label="Illustration of a mischievous cartoon sun aiming a bow and arrow"></div>

  <div class="legend">
    <div class="legend-row">
      <div class="legend-tiles">
        <div class="towel" role="img" aria-label="Woman on a towel, no skin cancer"></div>
        <div class="towel" role="img" aria-label="Man on a towel, no skin cancer"></div>
      </div>
      <span class="legend-label">= no skin cancer</span>
    </div>
    <div class="legend-row">
      <div class="legend-tiles">
        <div class="towel skin" role="img" aria-label="Sunburned woman on a towel, skin cancer"></div>
        <div class="towel skin" role="img" aria-label="Sunburned man on a towel, skin cancer"></div>
      </div>
      <span class="legend-label">= skin cancer</span>
    </div>
    <div class="legend-row">
      <div class="legend-tiles">
        <div class="towel melanoma" role="img" aria-label="Woman struck by an arrow, melanoma"></div>
        <div class="towel melanoma" role="img" aria-label="Man struck by an arrow, melanoma"></div>
      </div>
      <span class="legend-label">= melanoma</span>
    </div>
  </div>

  <div class="beach-grid" role="img" aria-label="100 sunbathers on towels: 17 with skin cancer and 3 with melanoma">
    <div class="towel"></div><div class="towel"></div><div class="towel"></div><div class="towel"></div><div class="towel skin"></div><div class="towel"></div><div class="towel"></div><div class="towel skin"></div><div class="towel"></div><div class="towel"></div>
    <div class="towel"></div><div class="towel"></div><div class="towel skin"></div><div class="towel"></div><div class="towel"></div><div class="towel"></div><div class="towel melanoma"></div><div class="towel"></div><div class="towel"></div><div class="towel skin"></div>
    <div class="towel"></div><div class="towel skin"></div><div class="towel"></div><div class="towel"></div><div class="towel skin"></div><div class="towel"></div><div class="towel skin"></div><div class="towel"></div><div class="towel"></div><div class="towel"></div>
    <div class="towel"></div><div class="towel"></div><div class="towel"></div><div class="towel"></div><div class="towel"></div><div class="towel melanoma"></div><div class="towel"></div><div class="towel"></div><div class="towel"></div><div class="towel"></div>
    <div class="towel"></div><div class="towel"></div><div class="towel skin"></div><div class="towel"></div><div class="towel"></div><div class="towel"></div><div class="towel"></div><div class="towel skin"></div><div class="towel"></div><div class="towel"></div>
    <div class="towel"></div><div class="towel"></div><div class="towel"></div><div class="towel"></div><div class="towel melanoma"></div><div class="towel"></div><div class="towel"></div><div class="towel skin"></div><div class="towel"></div><div class="towel"></div>
    <div class="towel skin"></div><div class="towel"></div><div class="towel"></div><div class="towel"></div><div class="towel"></div><div class="towel"></div><div class="towel"></div><div class="towel"></div><div class="towel"></div><div class="towel skin"></div>
    <div class="towel"></div><div class="towel"></div><div class="towel"></div><div class="towel"></div><div class="towel skin"></div><div class="towel skin"></div><div class="towel"></div><div class="towel"></div><div class="towel"></div><div class="towel"></div>
    <div class="towel"></div><div class="towel"></div><div class="towel"></div><div class="towel"></div><div class="towel"></div><div class="towel"></div><div class="towel"></div><div class="towel skin"></div><div class="towel"></div><div class="towel"></div>
    <div class="towel"></div><div class="towel"></div><div class="towel skin"></div><div class="towel"></div><div class="towel"></div><div class="towel"></div><div class="towel"></div><div class="towel"></div><div class="towel"></div><div class="towel skin"></div>
  </div>

  <svg class="shore" viewBox="0 0 1200 508" preserveAspectRatio="none" aria-hidden="true">
    <defs>
      <linearGradient id="sea" x1="0" y1="0" x2="0" y2="1">
        <stop offset="0" stop-color="var(--sea-light)"/>
        <stop offset="1" stop-color="var(--sea-deep)"/>
      </linearGradient>
    </defs>
    <path d="M0 36 C80 20 150 44 240 34 C330 24 400 50 500 38 C600 26 680 52 780 40 C880 28 960 46 1060 30 C1120 22 1170 30 1200 26 L1200 508 L0 508 Z" fill="var(--foam)"/>
    <path d="M0 58 C90 44 160 70 250 58 C340 46 420 72 520 60 C620 48 700 74 800 62 C900 50 980 68 1080 52 C1130 46 1170 52 1200 48 L1200 508 L0 508 Z" fill="url(#sea)"/>
  </svg>
</body>
</html>
```